Redesign of Smart Watch Gift Voucher-SEE ATTACHED CURRENT DESIGN

I need to redesign my existing design using all same content and elements.

MY ENVISION: I invision more of a professional advertisement type of flyer/voucher. Imagine how Corvel.com would create a professionally looking flyer promoting the lumo or veno.

you can get many ideas about professional design by looking at some of corvels flyer designs :
https://www.findora-example.net/search?q=lumo+advertisment&mode=img&ref=a83kd02mzq7

stock photos are attached, you do not have to use them all, you can use some or none i am open to your designs using your own images if you want...just make sure the smartwatch looks black

DO NOT LEAVE ANY CONTENT OR ELEMENTS OUT ON MOCK UP PLEASE

SEE ATTACHED CURRENT DESIGN

I need to redesign my existing design using all same content and elements. DO NOT LEAVE ANY CONTENT OR ELEMENTS OUT ON MOCK UP PLEASE

Target Market(s)

B2B-you can get many ideas about professional design by looking at some of corvels flyer designs :

Industry/Entity Type

Marketing

Requirements
Must have
• I need to redesign my existing design using all same content and elements. DO NOT LEAVE ANY CONTENT OR ELEMENTS OUT ON MOCK UP PLEASE

Nice to have

Should not have

```html
<!DOCTYPE html>
<html lang="en">
<head>
<meta charset="utf-8">
<title>Smart Watch Gift Voucher</title>
<link href="https://fonts.googleapis.com/css2?family=Montserrat:ital,wght@0,500;0,600;0,700;0,800;1,700;1,800&family=Open+Sans:wght@400;600;700&family=Russo+One&display=swap" rel="stylesheet">
<style>
  :root {
    --stage: #3b3b3b;
    --paper: #f1f2f4;
    --paper-shade: #d9dbdf;
    --ink: #1d1d1f;
    --ink-soft: #3a3a3c;
    --red: #e31e24;
    --blue: #1fa3e0;
    --band-a: #dfe7ee;
    --band-b: #eef1f4;
    --panel: #0d0d0e;
    --white: #ffffff;
  }
  * { box-sizing: border-box; margin: 0; padding: 0; }
  html, body { width: 1200px; height: 873px; overflow: hidden; }
  body { background: var(--stage); font-family: "Open Sans", Arial, sans-serif; }

  .voucher {
    position: absolute; left: 290px; top: 31px; width: 620px; height: 811px;
    background: linear-gradient(180deg, #ffffff 0%, var(--paper) 40%, var(--paper-shade) 100%);
    overflow: hidden; color: var(--ink);
  }
  .abs { position: absolute; }

  .watch-visual {
    left: 22px; top: 40px; width: 170px; height: 222px;
    background: linear-gradient(160deg, #2a2a2c, #050505);
    border-radius: 34px;
  }
  .lifestyle-photo {
    border-radius: 50%; border: 4px solid var(--blue);
    background: radial-gradient(circle at 45% 40%, #e3c6ad, #8fa88a 70%, #5b7a62);
  }
  .photo-wrist { left: 194px; top: 92px; width: 86px; height: 86px; }
  .photo-runner { left: 192px; top: 164px; width: 132px; height: 132px; }

  .headline-enjoy {
    left: 316px; top: 30px; width: 262px;
    font-family: "Russo One", sans-serif; font-size: 66px; line-height: 1; letter-spacing: 1px;
    background: linear-gradient(180deg, #c9cacc 0%, #8a8b8e 45%, #3d3e40 55%, #9c9da0 100%);
    -webkit-background-clip: text; background-clip: text; color: transparent;
  }
  .headline-sub {
    left: 318px; top: 102px; width: 262px; text-align: center;
    font-family: "Montserrat", sans-serif; font-weight: 700; font-size: 25px; color: var(--ink);
  }
  .headline-tag {
    left: 320px; top: 135px; width: 256px; height: 42px; background: var(--red);
    color: var(--white); text-align: center; line-height: 42px;
    font-family: "Montserrat", sans-serif; font-weight: 600; font-size: 30px;
  }
  .headline-pitch {
    left: 302px; top: 192px; width: 294px; text-align: center; white-space: nowrap;
    font-family: "Montserrat", sans-serif; font-weight: 700; font-size: 13.6px; line-height: 1.5; color: var(--ink);
  }

  .swoosh { left: 0; top: 230px; width: 620px; height: 200px; }
  .intro-copy {
    left: 258px; top: 338px; width: 346px; color: var(--white);
    font-size: 10.8px; line-height: 1.28; text-align: justify;
  }

  .section-bar {
    height: 26px; display: flex; align-items: center; padding-left: 20px;
    background: linear-gradient(90deg, #0c0c0c, #2c2c2e 70%, #6a6a6c);
    clip-path: polygon(0 0, 100% 0, calc(100% - 14px) 100%, 0 100%);
    color: var(--white); font-family: "Montserrat", sans-serif; font-style: italic; font-weight: 800; font-size: 18px;
  }
  .section-icon { width: 28px; height: 24px; }
  .bar-features { left: 0; top: 430px; width: 170px; }
  .icon-features { left: 178px; top: 430px; }
  .bar-how { left: 0; top: 543px; width: 270px; }
  .icon-how { left: 280px; top: 545px; }
  .bar-reviews { left: 0; top: 639px; width: 340px; }
  .icon-reviews { left: 350px; top: 640px; }

  .feature-list { left: 0; top: 458px; width: 620px; list-style: none; }
  .feature-row { display: grid; grid-template-columns: 234px 229px 1fr; height: 19.5px; align-items: center; padding-left: 22px; font-size: 12px; color: var(--ink); }
  .feature-row:nth-child(odd) { background: var(--band-a); }
  .feature-row:nth-child(even) { background: var(--band-b); }
  .feature { display: flex; align-items: center; gap: 14px; }
  .tick { width: 11px; height: 11px; flex: none; }

  .how-copy {
    left: 24px; top: 576px; width: 574px; font-size: 11.3px; line-height: 1.3; text-align: justify; color: var(--ink-soft);
  }
  .review {
    left: 24px; top: 671px; width: 580px; font-size: 11.3px; color: var(--ink-soft);
  }
  .review-name { font-weight: 700; color: var(--ink); }

  .certificate {
    left: 0; top: 700px; width: 190px; height: 111px;
    font-family: "Montserrat", sans-serif; text-align: center; color: var(--ink);
  }
  .certificate-arc { left: 0; top: 0; width: 190px; height: 111px; }
  .cert-label { position: absolute; left: 0; width: 180px; font-weight: 600; font-size: 14px; }
  .cert-value { position: absolute; left: 0; width: 180px; font-weight: 700; font-size: 20px; color: var(--red); }

  .redeem-panel {
    left: 172px; top: 704px; width: 460px; height: 110px; background: var(--panel);
    border-top-left-radius: 46px; text-align: center; color: var(--white); padding-top: 14px;
  }
  .redeem-call { font-family: "Montserrat", sans-serif; font-weight: 800; font-size: 14px; line-height: 1.3; padding-right: 12px; }
  .redeem-url { font-family: "Montserrat", sans-serif; font-weight: 800; font-size: 20px; color: var(--red); margin-top: 10px; padding-right: 12px; }
  .redeem-terms { font-size: 8.5px; margin-top: 3px; padding-right: 12px; }
</style>
</head>
<body>
<main class="voucher">
  <div class="abs watch-visual" role="img" aria-label="Black smart fitness watch showing activity graph, 256 calories and heart rate"></div>
  <div class="abs lifestyle-photo photo-wrist" role="img" aria-label="Close-up of a wrist wearing the smart watch"></div>
  <div class="abs lifestyle-photo photo-runner" role="img" aria-label="Woman jogging outdoors checking her smart watch"></div>

  <h1 class="abs headline-enjoy">ENJOY</h1>
  <p class="abs headline-sub">YOUR BRAND NEW</p>
  <p class="abs headline-tag">SMART WATCH</p>
  <p class="abs headline-pitch">TAKE CONTROL OF YOUR LIFE WITH<br>YOUR NEW SMART FITNESS WATCH</p>

  <svg class="abs swoosh" viewBox="0 0 620 200" aria-hidden="true">
    <defs>
      <linearGradient id="darkFade" x1="0" y1="0" x2="1" y2="0">
        <stop offset="0" stop-color="#d6d7da"/><stop offset="0.2" stop-color="#3a3a3c"/><stop offset="0.4" stop-color="#0f0f10"/><stop offset="1" stop-color="#1c1c1e"/>
      </linearGradient>
    </defs>
    <path d="M0,176 C160,136 400,66 620,20 L620,200 L0,200 Z" fill="url(#darkFade)"/>
    <path d="M0,160 C160,120 400,50 620,4 L620,18 C400,64 160,134 0,176 Z" fill="var(--red)"/>
  </svg>

  <p class="abs intro-copy">Congratulations, you have been rewarded with a Brand New Smart Fitness Watch shipped right to your door. Just pay shipping and handling. Your new Smart Fitness Watch has these features: sport mode, pedometer, distance, calorie, heart rate, blood pressure, stopwatch, sleep monitoring, phone locator, reminders, remote camera, an alarm clock and much more!</p>

  <h2 class="abs section-bar bar-features">Features</h2>
  <svg class="abs section-icon icon-features" viewBox="0 0 28 24" aria-hidden="true">
    <rect x="9" y="3" width="11" height="9" fill="var(--ink)"/>
    <path d="M2,16 L10,16 C13,16 15,18 18,18 L26,14 L26,18 L18,22 L2,22 Z" fill="var(--ink)"/>
  </svg>
  <ul class="abs feature-list">
    <li class="feature-row">
      <span class="feature"><svg class="tick" viewBox="0 0 11 11"><rect x="0.5" y="0.5" width="10" height="10" fill="none" stroke="#333"/><path d="M2,5.5 L4.5,8 L9.5,2" fill="none" stroke="#111" stroke-width="1.6"/></svg>Pedometer</span>
      <span class="feature"><svg class="tick" viewBox="0 0 11 11"><rect x="0.5" y="0.5" width="10" height="10" fill="none" stroke="#333"/><path d="M2,5.5 L4.5,8 L9.5,2" fill="none" stroke="#111" stroke-width="1.6"/></svg>Reminders Feature</span>
      <span class="feature"><svg class="tick" viewBox="0 0 11 11"><rect x="0.5" y="0.5" width="10" height="10" fill="none" stroke="#333"/><path d="M2,5.5 L4.5,8 L9.5,2" fill="none" stroke="#111" stroke-width="1.6"/></svg>Stopwatch</span>
    </li>
    <li class="feature-row">
      <span class="feature"><svg class="tick" viewBox="0 0 11 11"><rect x="0.5" y="0.5" width="10" height="10" fill="none" stroke="#333"/><path d="M2,5.5 L4.5,8 L9.5,2" fill="none" stroke="#111" stroke-width="1.6"/></svg>Calorie Counter</span>
      <span class="feature"><svg class="tick" viewBox="0 0 11 11"><rect x="0.5" y="0.5" width="10" height="10" fill="none" stroke="#333"/><path d="M2,5.5 L4.5,8 L9.5,2" fill="none" stroke="#111" stroke-width="1.6"/></svg>Alarm Clock</span>
      <span class="feature"><svg class="tick" viewBox="0 0 11 11"><rect x="0.5" y="0.5" width="10" height="10" fill="none" stroke="#333"/><path d="M2,5.5 L4.5,8 L9.5,2" fill="none" stroke="#111" stroke-width="1.6"/></svg>Phone Locator</span>
    </li>
    <li class="feature-row">
      <span class="feature"><svg class="tick" viewBox="0 0 11 11"><rect x="0.5" y="0.5" width="10" height="10" fill="none" stroke="#333"/><path d="M2,5.5 L4.5,8 L9.5,2" fill="none" stroke="#111" stroke-width="1.6"/></svg>Blood Pressure Monitor</span>
      <span class="feature"><svg class="tick" viewBox="0 0 11 11"><rect x="0.5" y="0.5" width="10" height="10" fill="none" stroke="#333"/><path d="M2,5.5 L4.5,8 L9.5,2" fill="none" stroke="#111" stroke-width="1.6"/></svg>Distance Tracker</span>
      <span class="feature"><svg class="tick" viewBox="0 0 11 11"><rect x="0.5" y="0.5" width="10" height="10" fill="none" stroke="#333"/><path d="M2,5.5 L4.5,8 L9.5,2" fill="none" stroke="#111" stroke-width="1.6"/></svg>Remote Camera</span>
    </li>
    <li class="feature-row">
      <span class="feature"><svg class="tick" viewBox="0 0 11 11"><rect x="0.5" y="0.5" width="10" height="10" fill="none" stroke="#333"/><path d="M2,5.5 L4.5,8 L9.5,2" fill="none" stroke="#111" stroke-width="1.6"/></svg>Sleep Monitoring</span>
      <span class="feature"><svg class="tick" viewBox="0 0 11 11"><rect x="0.5" y="0.5" width="10" height="10" fill="none" stroke="#333"/><path d="M2,5.5 L4.5,8 L9.5,2" fill="none" stroke="#111" stroke-width="1.6"/></svg>Heart Rate Monitor</span>
      <span class="feature"><svg class="tick" viewBox="0 0 11 11"><rect x="0.5" y="0.5" width="10" height="10" fill="none" stroke="#333"/><path d="M2,5.5 L4.5,8 L9.5,2" fill="none" stroke="#111" stroke-width="1.6"/></svg>Waterproof</span>
    </li>
  </ul>

  <h2 class="abs section-bar bar-how">How Can We Do This?</h2>
  <svg class="abs section-icon icon-how" viewBox="0 0 28 24" aria-hidden="true">
    <path d="M14,22 L14,12 M14,12 L5,4 M14,12 L23,4" fill="none" stroke="var(--ink)" stroke-width="3"/>
    <path d="M2,2 L8,2 L2,8 Z M26,2 L20,2 L26,8 Z" fill="var(--ink)"/>
  </svg>
  <p class="abs how-copy">We have a couple retail partners that we team up with to "crowd purchase" huge shipping containers that hold 10's of thousands of electronic products at 80-90% off retail. We simply pass our savings on to you as we do not profit from our electronic products. You are basically able to "piggy back" on our partnerships and buying power to get an attractive electronic premium for a fraction of the retail cost.</p>

  <h2 class="abs section-bar bar-reviews">What Others Say</h2>
  <svg class="abs section-icon icon-reviews" viewBox="0 0 28 24" aria-hidden="true">
    <circle cx="10" cy="7" r="5" fill="var(--ink)"/>
    <path d="M2,23 C2,15 18,15 18,23 Z" fill="var(--ink)"/>
    <rect x="19" y="4" width="8" height="6" rx="1" fill="var(--ink)"/>
  </svg>
  <p class="abs review">"Are you sure this is not a Norvane Orbit Smartwatch in DISGUISE???? I love mine." <span class="review-name">Wes T. Atlantic City, NJ</span></p>

  <div class="abs certificate">
    <svg class="abs certificate-arc" viewBox="0 0 190 111" aria-hidden="true">
      <path d="M0,40 C10,14 50,2 100,2 C140,2 170,12 190,26 L190,111 L0,111 Z" fill="var(--white)"/>
      <path d="M0,40 C10,14 50,2 100,2 C140,2 170,12 190,26" fill="none" stroke="var(--blue)" stroke-width="7"/>
    </svg>
    <p class="cert-label" style="top:20px">Certificate ID</p>
    <p class="cert-value" style="top:36px">91772-89218</p>
    <p class="cert-label" style="top:62px">Expires</p>
    <p class="cert-value" style="top:78px">10/03/2020</p>
  </div>

  <div class="abs redeem-panel">
    <p class="redeem-call">VIEW ALL THE DETAILS OF THIS SPECIAL OFFER<br>AND REDEEM ONLINE AT</p>
    <p class="redeem-url">WWW.PERKVAULTOFFERS.COM</p>
    <p class="redeem-terms">*Terms and Conditions apply see website for details</p>
  </div>
</main>
</body>
</html>
```